Quorvel Lab - Business Cards & Stationary
Layouts for B-cards, Letterhead, Powerpoint Templates
Quorvel Lab - Business Cards & Stationary -
Creative Brief
Professional
Desmond Pelly
Director of Product Development
4852 Amberfield Lane Dallas, Texas 75391-4418
des.pelly@quorvellabs.example

```html
<!DOCTYPE html>
<html lang="en">
<head>
<meta charset="utf-8">
<title>Quorvel Lab – Business Card</title>
<link rel="stylesheet" href="https://fonts.googleapis.com/css2?family=Source+Sans+3:wght@400;600;700&display=swap">
<style>
  :root {
    --page-bg: #d9d9d9;
    --card-bg: #ffffff;
    --brand-gold: #8a6a2a;
    --accent-red: #b5121b;
    --accent-red-dark: #5e0a0e;
    --text-grey: #555555;
    --text-dark: #333333;
  }
  html, body {
    margin: 0;
    padding: 0;
    width: 1200px;
    height: 1035px;
    overflow: hidden;
    background: var(--page-bg);
    font-family: "Source Sans 3", "Myriad Pro", Arial, sans-serif;
  }
  .business-card {
    position: absolute;
    left: 100px;
    top: 232px;
    width: 1000px;
    height: 571px;
    background: var(--card-bg);
    border-radius: 34px;
    box-shadow: 0 8px 24px rgba(0, 0, 0, 0.18);
    overflow: hidden;
  }
  .brand {
    position: absolute;
    left: 58px;
    top: 104px;
    display: flex;
    align-items: center;
    gap: 18px;
  }
  .brand-mark {
    width: 70px;
    height: 70px;
    border-radius: 50%;
    background: var(--brand-gold);
  }
  .brand-name {
    font-size: 76px;
    font-weight: 600;
    color: var(--brand-gold);
    line-height: 1;
    letter-spacing: -0.5px;
  }
  .person {
    position: absolute;
    left: 520px;
    top: 288px;
  }
  .person-name {
    margin: 0;
    font-size: 38px;
    font-weight: 700;
    color: var(--accent-red);
    line-height: 1.1;
  }
  .person-title {
    margin: 2px 0 0;
    font-size: 17px;
    color: var(--text-grey);
  }
  .contact {
    position: absolute;
    left: 64px;
    top: 398px;
    font-size: 16px;
    line-height: 1.4;
    color: var(--text-grey);
  }
  .contact p { margin: 0; }
  .contact .address { margin-bottom: 12px; }
  .contact .label {
    display: inline-block;
    width: 48px;
    font-weight: 700;
    color: var(--text-dark);
  }
  .edge-tab {
    position: absolute;
    left: 0;
    top: 408px;
    width: 14px;
    height: 92px;
    background: linear-gradient(90deg, var(--accent-red-dark), var(--accent-red));
  }
</style>
</head>
<body>
  <div class="business-card">
    <div class="brand">
      <span class="brand-mark"></span>
      <span class="brand-name">Quorvel Lab</span>
    </div>

    <div class="person">
      <h1 class="person-name">Desmond Pelly</h1>
      <p class="person-title">Director of Product Development</p>
    </div>

    <div class="edge-tab"></div>

    <div class="contact">
      <div class="address">
        <p>4852 Amberfield Lane</p>
        <p>Dallas, Texas 75391-4418</p>
      </div>
      <p><span class="label">Cell</span>: 214.555.0187</p>
      <p><span class="label">Email</span>: des.pelly@quorvellabs.example</p>
    </div>
  </div>
</body>
</html>
```